SKYVANTIX (drone photo and video) and Photogrammetry Services (mapping and 3D modeling)

We need a business card design for a SKYVANTIX. Our businesses provides (drone) Aerial Photo and Video Captures. However we also provide Photogrammetry (which is 3D modeling and mapping). We greatly value unique points of view taken of landscapes and subjects with aerial photography and videography. 3D modeling and mapping is the other area of focus and have an incredibly broad scope of applications and imaginative creativity.

Target Market(s)

Based out of Northern Virginia and serving the greater Virginia and Maryland areas

Industry/Entity Type

Drone Photo and video and Photogrammetry Services (mapping and 3D modeling)

Contact Information for Business Card

3D Models, Maps and Photo/Video Production name: Marcus Pellerin email: mtp@skyvantix.us website: skyvantix.us phone: 571-389-6043; please also include "Aerial Photo/Video and 3D Mapping/Modeling"

Requirements
Must have
• Please make this design vertical and double sided. The selection box is not letting me choose Double Sided but that is my wish. Incorporate uploaded LOGO and color scheme
Nice to have
• Preferably does not feel too crowded and balances not having an exaggerated amount of distracting detail
Should not have
• do not cram bullet points or text in long form

```html
<!DOCTYPE html>
<html lang="en">
<head>
<meta charset="utf-8">
<title>SKYVANTIX — Business Card</title>
<link href="https://fonts.googleapis.com/css2?family=Montserrat:wght@400;500;700&family=Oswald:wght@500&display=swap" rel="stylesheet">
<style>
  :root {
    --stage: #2b2b2d;
    --card: #0b0b0c;
    --card-edge: #1a1a1c;
    --white: #ffffff;
    --orange: #f7931e;
    --amber: #fbb829;
    --red: #f0282d;
    --deep-orange: #ff5a1f;
  }
  * { box-sizing: border-box; margin: 0; padding: 0; }
  html, body {
    width: 1200px; height: 1200px; overflow: hidden;
    background: var(--stage);
  }
  .stage {
    position: relative; width: 1200px; height: 1200px;
    display: flex; justify-content: center; align-items: center; gap: 70px;
  }
  .card {
    position: relative; width: 440px; height: 770px;
    background: linear-gradient(160deg, var(--card) 0%, var(--card) 55%, var(--card-edge) 100%);
    overflow: hidden;
    box-shadow: 0 18px 40px rgba(0,0,0,.45);
    font-family: "Montserrat", sans-serif;
    color: var(--white);
  }
  .card__bar {
    position: absolute; left: 0; right: 0; bottom: 0; height: 16px;
    background: linear-gradient(90deg, var(--red) 0%, var(--deep-orange) 25%, var(--amber) 50%, var(--orange) 75%, var(--red) 100%);
  }
  .brand {
    display: flex; align-items: center; justify-content: center; gap: 14px;
  }
  .brand__dot {
    width: 34px; height: 34px; border-radius: 50%;
    background: var(--orange);
  }
  .brand__name {
    font-family: "Montserrat", sans-serif; font-weight: 700;
    font-size: 48px; letter-spacing: 1px; color: var(--white);
  }
  .card--front .brand { position: absolute; left: 0; right: 0; top: 300px; }
  .card--front .tagline {
    position: absolute; left: 0; right: 0; bottom: 46px;
    text-align: center;
    font-family: "Oswald", sans-serif; font-weight: 500;
    font-size: 21px; letter-spacing: .5px; text-transform: uppercase;
  }
  .card--back .brand { position: absolute; left: 0; right: 0; top: 170px; }
  .contact {
    position: absolute; left: 70px; top: 440px;
  }
  .contact__name {
    font-weight: 700; font-size: 34px; letter-spacing: .5px;
    color: var(--orange); text-transform: uppercase; margin-bottom: 30px;
  }
  .contact__list { list-style: none; }
  .contact__item {
    display: flex; align-items: center; gap: 16px;
    font-size: 24px; font-weight: 400; margin-bottom: 20px;
  }
  .contact__icon { width: 40px; height: 40px; flex: none; }
</style>
</head>
<body>
<main class="stage">
  <svg width="0" height="0" style="position:absolute" aria-hidden="true">
    <defs>
      <linearGradient id="icon-fill" x1="0" y1="0" x2="1" y2="1">
        <stop offset="0" stop-color="#fbb829"/>
        <stop offset="1" stop-color="#f0282d"/>
      </linearGradient>
    </defs>
  </svg>

  <section class="card card--front" aria-label="Card front">
    <div class="brand">
      <span class="brand__dot"></span>
      <span class="brand__name">SKYVANTIX</span>
    </div>
    <p class="tagline">Aerial Photo/Video and 3D Mapping/Modeling</p>
    <div class="card__bar"></div>
  </section>

  <section class="card card--back" aria-label="Card back">
    <div class="brand">
      <span class="brand__dot"></span>
      <span class="brand__name">SKYVANTIX</span>
    </div>
    <div class="contact">
      <h1 class="contact__name">Marcus Pellerin</h1>
      <ul class="contact__list">
        <li class="contact__item">
          <svg class="contact__icon" viewBox="0 0 40 40" aria-hidden="true">
            <circle cx="20" cy="20" r="20" fill="url(#icon-fill)"/>
            <path d="M13 12c1-1 2-1 3 0l2 3c.6 1 .3 1.8-.5 2.4l-1 .8c1 2.4 2.8 4.2 5.2 5.2l.8-1c.6-.8 1.4-1.1 2.4-.5l3 2c1 1 1 2 0 3l-1.5 1.5C23 30 10 17 11.5 13.5z" fill="#111"/>
          </svg>
          <span>571-389-6043</span>
        </li>
        <li class="contact__item">
          <svg class="contact__icon" viewBox="0 0 40 40" aria-hidden="true">
            <circle cx="20" cy="20" r="20" fill="url(#icon-fill)"/>
            <g fill="none" stroke="#111" stroke-width="1.8">
              <circle cx="20" cy="20" r="10"/>
              <ellipse cx="20" cy="20" rx="4.5" ry="10"/>
              <line x1="10" y1="20" x2="30" y2="20"/>
              <line x1="12" y1="14.5" x2="28" y2="14.5"/>
              <line x1="12" y1="25.5" x2="28" y2="25.5"/>
            </g>
          </svg>
          <span>skyvantix.us</span>
        </li>
        <li class="contact__item">
          <svg class="contact__icon" viewBox="0 0 40 40" aria-hidden="true">
            <circle cx="20" cy="20" r="20" fill="url(#icon-fill)"/>
            <g fill="none" stroke="#111" stroke-width="1.8" stroke-linejoin="round">
              <rect x="10" y="13" width="20" height="14"/>
              <polyline points="10,13 20,21 30,13"/>
            </g>
          </svg>
          <span>mtp@skyvantix.us</span>
        </li>
      </ul>
    </div>
    <div class="card__bar"></div>
  </section>
</main>
</body>
</html>
```